VEXMORA, INC. BUSINESS CARD REDESIGN

Attached is an example business card. Name, Title, Address, Contact Information, logo and social media icons are ALL required to be designed into the card. The logo can be modified. An exact replica (or few modifications) of the existing design will be rejected.

Card can either have a blue or white background. Blues and any complimentary color of social media logos that are included on the card.

An example is attached/provided but should not be merely copied or slightly modified.

This should be a new, innovative design relative to the general concept of the existing business card.

Reason: This project has been updated; please utilize the original logo as much as possible. Also because of the high quality of most of the submissions the company requires additional time to reach out with feedback to the top designers for editing and re-submission to determine the finalist. Thank you.

Target Market(s)

B2B (business to business), Television News Stations, Broadcasting, Radio, Magazine and Newspaper Organizations.

Industry/Entity Type

Media

Contact Information for Business Card

Example attached. Company name with exisiting logo (can be altered/edited) in blue (similar to quorble/lintavo blue, but brighter and/or bolder).

Optional two sided card so that just the "VEXMORA" logo is on the front side of the card with contact information on the back side.

Logo Text

VEXMORA

Font styles to use
Sans Serif
Other font styles liked:
• ubuntu, ubuntu bold etc...or similar clean fonts that look great on mobile. Open to use of Google Fonts.

Requirements
Must have
• Must have the following branding integrated into the design (not in any specefic order or verbatim):
• VEXMORA, INC.
• Milo Brandt CEO & Founder
• 83 Wrenfield Nashville, TN 37210
• mobile: 615.555.0142
• milo@vexmora-mail.test
• https://vexmora-mail.test
• Must also include brand assests (e.g. official logos) of QUORBLE, LINTAVO, MARQEEN, SOLLIVAR, DREVONIX, and KELMITRU
• A clean logo only on the front side is requested (blue or white background). The front side can incorporate the social media icons listed in the brief if designer chooses.
Nice to have
• Card can either have a blue or white background. Blues and any complimentary color of social media logos that are included on the card.
• The card can be double sided so that the logo is on front and contact information is professionally displayed on the back. Not necessarily a requirement but a double-sided design will receive a higher preference.
• An example is attached/provided but should not be merely copied or slightly modified.
• This should be a new, innovative design relative to the general concept of the existing business card.
• Also the brand name with the TM trademark after: for example, Vexmora™
• This (the tm) should be added only after a standalone use of just the word VEXMORA or Vexmora™ AND not Vexmora™, Inc., included in the URL or email address obviously. Thanks :)
Should not have
• Should not have the text spelling of Lintavo, Drevonix, Sollivar, Kelmitru, etc...with the exception of "Marqeen" as it is the approved logo to be integrated.

```html
<!DOCTYPE html>
<html lang="en">
<head>
<meta charset="utf-8">
<title>Vexmora™ Business Card</title>
<link rel="stylesheet" href="https://fonts.googleapis.com/css2?family=Ubuntu:wght@400;500;700&display=swap">
<style>
  :root {
    --stage: #939396;
    --brand-blue: #3b52a3;
    --brand-blue-tint: #5165b0;
    --paper: #ffffff;
    --paper-tint: #f1f2f5;
    --ink-grey: #4a4a4a;
    --shadow: rgba(0, 0, 0, 0.35);
  }
  html, body {
    margin: 0;
    padding: 0;
    width: 1200px;
    height: 1000px;
    overflow: hidden;
    background: var(--stage);
    font-family: "Ubuntu", sans-serif;
  }
  .canvas {
    position: relative;
    width: 1200px;
    height: 1000px;
  }
  .card {
    position: absolute;
    left: 275px;
    width: 652px;
    height: 381px;
    overflow: hidden;
    box-shadow: 4px 5px 6px var(--shadow);
  }
  .card--front { top: 102px; background: var(--brand-blue); }
  .card--back  { top: 535px; background: var(--paper); }

  .card__pattern {
    position: absolute;
    inset: 0;
  }
  .card--front .card__pattern { background: linear-gradient(135deg, var(--brand-blue-tint), var(--brand-blue)); opacity: 0.55; }
  .card--back .card__pattern { background: linear-gradient(135deg, var(--paper-tint), var(--paper)); }

  /* Front */
  .front-mark {
    position: absolute;
    left: 0; right: 0;
    top: 118px;
    display: flex;
    flex-direction: column;
    align-items: center;
  }
  .front-mark__square {
    width: 76px;
    height: 76px;
    border-radius: 6px;
    background: var(--paper);
  }
  .front-mark__name {
    margin-top: 12px;
    font-weight: 700;
    font-size: 46px;
    line-height: 1;
    color: var(--paper);
    letter-spacing: 0.5px;
  }
  .tm { font-size: 0.32em; vertical-align: 1.9em; font-weight: 700; }

  /* Back */
  .back-mark {
    position: absolute;
    left: 26px;
    top: 58px;
    width: 142px;
    display: flex;
    flex-direction: column;
    align-items: center;
  }
  .back-mark__square {
    width: 60px;
    height: 56px;
    border-radius: 4px;
    background: var(--brand-blue);
  }
  .back-mark__name {
    margin-top: 8px;
    font-weight: 700;
    font-size: 30px;
    line-height: 1;
    color: var(--brand-blue);
  }
  .person {
    position: absolute;
    left: 202px;
    top: 114px;
  }
  .person__name {
    margin: 0;
    font-weight: 500;
    font-size: 32px;
    line-height: 1;
    color: var(--brand-blue);
  }
  .person__title {
    margin: 6px 0 0;
    font-weight: 500;
    font-size: 18px;
    color: var(--ink-grey);
  }
  .contact-list {
    position: absolute;
    left: 202px;
    top: 193px;
    margin: 0;
    padding: 0;
    list-style: none;
  }
  .contact-list__item {
    display: flex;
    align-items: center;
    height: 23px;
    font-size: 16px;
    color: var(--ink-grey);
  }
  .contact-list__icon {
    width: 18px;
    height: 18px;
    margin-right: 8px;
    flex: none;
  }
  .social-row {
    position: absolute;
    right: 34px;
    bottom: 36px;
    display: flex;
    align-items: flex-end;
    gap: 6px;
    margin: 0;
    padding: 0;
    list-style: none;
  }
  .social-row__badge {
    width: 28px;
    height: 28px;
    border-radius: 4px;
    background: var(--brand-blue);
  }
  .social-row__label {
    height: 28px;
    display: flex;
    align-items: center;
    font-weight: 700;
    font-size: 10px;
    color: var(--brand-blue);
  }
</style>
</head>
<body>
<main class="canvas">
  <section class="card card--front" aria-label="Card front">
    <div class="card__pattern" role="img" aria-label="Faint repeating pattern of the brand mark across the card"></div>
    <div class="front-mark">
      <div class="front-mark__square"></div>
      <div class="front-mark__name">vexmora<span class="tm">™</span></div>
    </div>
  </section>

  <section class="card card--back" aria-label="Card back">
    <div class="card__pattern" role="img" aria-label="Faint repeating pattern of the brand mark across the card"></div>
    <div class="back-mark">
      <div class="back-mark__square"></div>
      <div class="back-mark__name">vexmora<span class="tm">™</span></div>
    </div>

    <div class="person">
      <h1 class="person__name">Milo Brandt</h1>
      <p class="person__title">CEO &amp; Founder</p>
    </div>

    <ul class="contact-list">
      <li class="contact-list__item">
        <svg class="contact-list__icon" viewBox="0 0 18 18" aria-hidden="true">
          <circle cx="9" cy="9" r="9" fill="var(--brand-blue)"/>
          <path d="M9 3.6a3.4 3.4 0 0 0-3.4 3.4c0 2.5 3.4 7 3.4 7s3.4-4.5 3.4-7A3.4 3.4 0 0 0 9 3.6z" fill="#fff"/>
          <circle cx="9" cy="7" r="1.3" fill="var(--brand-blue)"/>
        </svg>
        83 Wrenfield Nashville, TN 37210
      </li>
      <li class="contact-list__item">
        <svg class="contact-list__icon" viewBox="0 0 18 18" aria-hidden="true">
          <circle cx="9" cy="9" r="9" fill="var(--brand-blue)"/>
          <rect x="6" y="3.5" width="6" height="11" rx="1.2" fill="#fff"/>
          <rect x="7" y="5" width="4" height="6.5" fill="var(--brand-blue)"/>
        </svg>
        615.555.0142
      </li>
      <li class="contact-list__item">
        <svg class="contact-list__icon" viewBox="0 0 18 18" aria-hidden="true">
          <circle cx="9" cy="9" r="9" fill="var(--brand-blue)"/>
          <rect x="4.2" y="5.5" width="9.6" height="7" rx="0.8" fill="#fff"/>
          <path d="M4.5 6l4.5 3.5L13.5 6" stroke="var(--brand-blue)" stroke-width="1" fill="none"/>
        </svg>
        milo@vexmora-mail.test
      </li>
      <li class="contact-list__item">
        <svg class="contact-list__icon" viewBox="0 0 18 18" aria-hidden="true">
          <circle cx="9" cy="9" r="9" fill="var(--brand-blue)"/>
          <circle cx="9" cy="9" r="4.6" fill="none" stroke="#fff" stroke-width="1.1"/>
          <ellipse cx="9" cy="9" rx="2" ry="4.6" fill="none" stroke="#fff" stroke-width="1"/>
          <line x1="4.4" y1="9" x2="13.6" y2="9" stroke="#fff" stroke-width="1"/>
        </svg>
        https://vexmora-mail.test
      </li>
    </ul>

    <ul class="social-row" aria-label="Social channels">
      <li class="social-row__badge" role="img" aria-label="Quorble channel badge"></li>
      <li class="social-row__badge" role="img" aria-label="Lintavo channel badge"></li>
      <li class="social-row__label">Marqeen</li>
      <li class="social-row__badge" role="img" aria-label="Sollivar channel badge"></li>
      <li class="social-row__badge" role="img" aria-label="Drevonix channel badge"></li>
      <li class="social-row__badge" role="img" aria-label="Kelmitru channel badge"></li>
      <li class="social-row__badge" role="img" aria-label="Vexmora channel badge"></li>
    </ul>
  </section>
</main>
</body>
</html>
```